Fiber Optic Internet flyer promotion Winter 2016-2017

I am looking for a marketing flyer that will not be folded, single sided that will advertise a Fiber Optic internet promotion that we are currently running.

The design should be clean, flow well, quickly grab attention, and if a very few short seconds list what the promotion is, and direct them to contact us.

It needs to list a few features of the promotion, but does not need to be in this order and should flow well with the flyer
1.) Fiber Optic Internet
2.) 100 Mbits for $140 /month or 150 Mbits for $190 /month
3.) Free construction cost up to $10,000, limited funds available.
4.) Limited time offer. Must commit before funds run out.

(555) 274-3916, www.kelvoranet.example

Target Market(s)

Small to large business

Industry/Entity Type

Internet Service Provider

Requirements
Must have
• Eye catching appeal. Quickly convey the message of the promotion and our company name and phone number.
Should not have
• Our company is primarily a wireless ISP. This promotion is all about Fiber Optic. I do not want to draw attention to the "wireless" portion of our business with this flyer.

```html
<!DOCTYPE html>
<html lang="en">
<head>
<meta charset="utf-8">
<title>Fiber Optic Internet Flyer</title>
<link href="https://fonts.googleapis.com/css2?family=Arimo:wght@400;700&display=swap" rel="stylesheet">
<style>
  :root {
    --stage: #e9e6e1;
    --navy: #142f4e;
    --sky: #4a8fcb;
    --sky-light: #7fb6e6;
    --red: #d41f35;
    --white: #ffffff;
    --photo-deep: #0b2140;
  }
  * { box-sizing: border-box; margin: 0; padding: 0; }
  html, body { width: 1200px; height: 864px; overflow: hidden; background: var(--stage); }
  body { font-family: "Arimo", Arial, sans-serif; color: var(--white); }

  .flyer {
    position: absolute; left: 303px; top: 12px;
    width: 594px; height: 840px;
    background: var(--navy);
    overflow: hidden;
    box-shadow: 0 4px 18px rgba(0,0,0,.25);
  }

  .cable-photo {
    position: absolute; left: 0; top: 480px; width: 594px; height: 360px;
    background:
      radial-gradient(ellipse at 78% 55%, rgba(220,235,255,.85) 0%, rgba(111,166,222,.55) 22%, transparent 55%),
      linear-gradient(160deg, #1a3e6c 0%, var(--photo-deep) 55%, #12335c 100%);
  }

  .headline {
    position: absolute; left: 128px; top: 14px; width: 338px; height: 120px;
    background: var(--sky);
    text-align: center; font-weight: 700; font-size: 44px; line-height: 48px;
    padding-top: 12px; letter-spacing: 0.5px;
  }

  .tag-string { position: absolute; left: 0; top: 0; }

  .price-tag {
    position: absolute; border-radius: 50%;
    border: 5px solid #0d2239;
    background: linear-gradient(180deg, var(--sky-light) 0%, var(--sky) 45%);
    overflow: hidden; text-align: center; font-weight: 700;
    box-shadow: 0 4px 10px rgba(0,0,0,.4);
  }
  .price-tag .speed { position: absolute; left: 0; right: 0; line-height: 1; }
  .price-tag .price-band {
    position: absolute; left: 0; right: 0; bottom: 0;
    background: var(--red); border-top: 4px solid var(--white);
  }
  .price-tag .amount { display: block; line-height: 1; }
  .price-tag .amount sup { font-size: .55em; vertical-align: .5em; }
  .price-tag .period { display: block; font-weight: 400; }

  .tag-100 { left: 54px; top: 196px; width: 244px; height: 244px; }
  .tag-100 .speed { top: 36px; font-size: 35px; }
  .tag-100 .price-band { height: 114px; padding-top: 4px; }
  .tag-100 .amount { font-size: 76px; }
  .tag-100 .period { font-size: 15px; }

  .tag-150 { left: 312px; top: 150px; width: 210px; height: 210px; }
  .tag-150 .speed { top: 30px; font-size: 31px; }
  .tag-150 .price-band { height: 98px; padding-top: 4px; }
  .tag-150 .amount { font-size: 64px; }
  .tag-150 .period { font-size: 13px; }

  .construction-note {
    position: absolute; left: 80px; top: 452px; width: 440px;
    text-align: center; font-weight: 700; font-size: 19px; line-height: 23px;
  }

  .phone-band {
    position: absolute; left: 300px; top: 506px; width: 294px; height: 62px;
    background: var(--red); font-weight: 700; font-size: 34px;
    line-height: 62px; text-align: center;
  }
  .offer-band {
    position: absolute; left: 0; top: 526px; width: 300px; height: 92px;
    background: var(--sky); font-weight: 700; font-size: 20px; line-height: 24px;
    padding: 10px 0 0 28px;
  }

  .brand {
    position: absolute; right: 34px; top: 700px;
    display: flex; align-items: center; gap: 10px;
  }
  .brand-dot { width: 26px; height: 26px; border-radius: 50%; background: var(--red); }
  .brand-name { font-weight: 700; font-size: 24px; color: var(--white); }

  .web-band {
    position: absolute; left: 0; top: 784px; width: 300px; height: 40px;
    background: var(--red); font-weight: 700; font-size: 19px;
    line-height: 40px; padding-left: 24px;
  }
</style>
</head>
<body>
  <article class="flyer">
    <div class="cable-photo" role="img" aria-label="Photo of network cable plugs in front of glowing fiber optic strands"></div>

    <svg class="tag-string" width="594" height="220" viewBox="0 0 594 220" aria-hidden="true">
      <path d="M172 134 L178 198" stroke="#d41f35" stroke-width="2" fill="none"/>
      <path d="M412 134 L416 152" stroke="#d41f35" stroke-width="2" fill="none"/>
    </svg>

    <h1 class="headline">FIBER OPTIC<br>INTERNET</h1>

    <div class="price-tag tag-100">
      <span class="speed">100<br>Mbits for</span>
      <div class="price-band">
        <span class="amount"><sup>$</sup>140</span>
        <span class="period">per month</span>
      </div>
    </div>

    <div class="price-tag tag-150">
      <span class="speed">150<br>Mbits for</span>
      <div class="price-band">
        <span class="amount"><sup>$</sup>190</span>
        <span class="period">per month</span>
      </div>
    </div>

    <p class="construction-note">Free construction cost up to $10,000,<br>limited funds available.</p>

    <div class="phone-band">(555) 274-3916</div>
    <p class="offer-band">Limited time offer.<br>Must commit before<br>funds run out.</p>

    <div class="brand">
      <span class="brand-dot"></span>
      <span class="brand-name">KELVORA NETWORKS</span>
    </div>

    <div class="web-band">www.kelvoranet.example</div>
  </article>
</body>
</html>
```